Lifestyle brand needs lip balm label design

We need a label design for lip balm tubes. The name of our company is "quorvalent"

Design Description:
Our lip balm tubes will be black. The label itself will be clear/transparent. We would like to create a gradient effect with the color green (same shade as our logo) starting from the bottom and slowly fading out to clear so that the black tube is visible (example of gradient shown in attached image)

We have two lip balm flavors: mint and lemongrass.
We would like the top/clear portion of the label to say "MINT" (all caps) . The second label should say "LEMONGRASS" (all caps) in the same location. Our logo "quorvalent" should be in the bottom/green portion of the label. Below the logo, we would like the words "NATURAL BALM" (all caps) in white text

```html
<!DOCTYPE html>
<html lang="en">
<head>
<meta charset="utf-8">
<title>Natural Balm Mint – Label</title>
<link rel="stylesheet" href="https://fonts.googleapis.com/css2?family=Montserrat:wght@300;400;600&display=swap">
<style>
  :root {
    --backdrop: #e8e8e8;
    --label-black: #000000;
    --brand-green: #619744;
    --text-white: #ffffff;
  }
  * { margin: 0; padding: 0; box-sizing: border-box; }
  html, body {
    width: 1200px;
    height: 960px;
    overflow: hidden;
    background: var(--backdrop);
  }
  .canvas {
    position: relative;
    width: 1200px;
    height: 960px;
  }
  .label {
    position: absolute;
    left: 200px;
    top: 80px;
    width: 800px;
    height: 800px;
    background: var(--label-black);
    overflow: hidden;
  }
  .label__corner-block {
    position: absolute;
    left: 296px;
    top: 0;
    width: 504px;
    height: 336px;
    background: var(--brand-green);
  }
  .label__base-bar {
    position: absolute;
    left: 0;
    bottom: 0;
    width: 253px;
    height: 43px;
    background: var(--brand-green);
  }
  .label__text {
    position: absolute;
    left: 0;
    width: 848px;
    text-align: center;
    color: var(--text-white);
    font-family: "Montserrat", sans-serif;
    white-space: nowrap;
  }
  .label__title {
    font-weight: 600;
    font-size: 80px;
    line-height: 1;
    letter-spacing: 1px;
  }
  .label__title--first { top: 380px; }
  .label__title--second { top: 473px; }
  .label__flavour {
    top: 562px;
    font-weight: 400;
    font-size: 31px;
    letter-spacing: 48px;
    text-indent: 48px;
    line-height: 1;
  }
  .label__brand {
    top: 620px;
    left: -34px;
    font-weight: 400;
    font-size: 92px;
    line-height: 1.1;
    letter-spacing: 0;
  }
</style>
</head>
<body>
  <main class="canvas">
    <section class="label" aria-label="Natural Balm Mint lip balm label">
      <div class="label__corner-block"></div>
      <div class="label__base-bar"></div>
      <p class="label__text label__title label__title--first">NATURAL</p>
      <p class="label__text label__title label__title--second">BALM</p>
      <p class="label__text label__flavour">MINT</p>
      <p class="label__text label__brand">quorvalent</p>
    </section>
  </main>
</body>
</html>
```